Hipster Hard Apple Cider - Bike / Gear / Cog Themed Label

Hard Apple Cider Label Needed:

- Looking for a retro, fun, funky, Venice Beach vibe.

- Design should incorporate bike/bicycle/wheel elements, appeal to both sexes and should be applicable to a can. (See can example in attachments).

- There should be a main brand logo that can stand alone in representing the brand and the feel of the brand. I envision a bike wheel, Sp*kes, gears, etc.

Please use brand name posted as JPG titled "Brand Name" in Attached Files:
>>> Tw*n* C*d*r

Target Market(s)

Our consumer is:
- Millennial
- Hipster
- Adventurous
- Active (biking/cycling)
- A craft beer + wine purchaser
- Unisex, veering towards masculine (65% male)

Industry/Entity Type

Wheel

Requirements
Must have
• - Bike elements that tie in the brand name (cogs, sp*kes, gears, bike frame, etc.)
• - A strong logo that can represent the brand

```html
<!DOCTYPE html>
<html lang="en">
<head>
<meta charset="utf-8">
<title>Twine Cider – Hard Apple Cider Label</title>
<link rel="stylesheet" href="https://fonts.googleapis.com/css2?family=Lobster&family=Oswald:wght@400;500;600;700&display=swap">
<style>
  :root {
    --page: #efeee9;
    --kraft: #e3c48f;
    --orange: #f28a23;
    --orange-deep: #d9731c;
    --ink: #2e2b28;
    --stripe: #b9a37c;
    --echo: #a08b68;
  }
  * { box-sizing: border-box; margin: 0; padding: 0; }
  html, body { width: 1200px; height: 1200px; overflow: hidden; background: var(--page); }
  .canvas { position: relative; width: 1200px; height: 1200px; overflow: hidden; background: var(--page); }

  .label { position: absolute; top: 210px; width: 496px; height: 834px; background: var(--kraft); }
  .label--front { left: 86px; }
  .label--back { left: 613px; }
  .label__art { position: absolute; inset: 0; width: 496px; height: 834px; }

  .wordmark {
    position: absolute; font-family: "Oswald", sans-serif; font-weight: 700;
    color: var(--ink); letter-spacing: -1px; white-space: nowrap; line-height: 1;
  }
  .label--front .wordmark { left: 62px; top: 56px; font-size: 44px; }
  .label--back .wordmark { left: 0; width: 496px; text-align: center; top: 38px; font-size: 34px; }

  .script {
    position: absolute; font-family: "Lobster", cursive; color: var(--ink);
    white-space: nowrap; line-height: 1;
  }
  .script--hard {
    left: 60px; top: 190px; width: 360px; text-align: center;
    font-size: 190px; transform: rotate(-22deg);
    text-shadow: 9px -6px 0 var(--echo);
  }
  .script--variety {
    left: 40px; top: 470px; width: 430px; text-align: center;
    font-size: 54px; transform: rotate(-4deg);
    text-shadow: 4px -3px 0 var(--echo);
  }

  .style-name {
    position: absolute; left: 188px; top: 690px; width: 100px; text-align: center;
    font-family: "Oswald", sans-serif; font-weight: 700; font-size: 44px;
    color: var(--ink); line-height: 1; letter-spacing: -1px;
  }
  .abv {
    position: absolute; left: 150px; top: 764px; display: flex; align-items: center; gap: 8px;
    font-family: "Oswald", sans-serif; font-weight: 500; font-size: 25px; color: var(--ink);
  }

  .warning {
    position: absolute; left: 24px; width: 448px; top: 120px; text-align: center;
    font-family: "Oswald", sans-serif; font-weight: 400; font-size: 16.5px;
    line-height: 21.5px; color: var(--ink); letter-spacing: -0.3px;
  }
  .back-note {
    position: absolute; left: 0; width: 496px; text-align: center;
    font-family: "Oswald", sans-serif; font-weight: 400; font-size: 21px;
    color: var(--ink); letter-spacing: -0.5px; line-height: 1;
  }
  .back-note--sulfites { top: 728px; }
  .back-note--bottler { top: 766px; }
</style>
</head>
<body>
<main class="canvas">

  <section class="label label--front">
    <svg class="label__art" viewBox="0 0 496 834" aria-hidden="true">
      <defs>
        <radialGradient id="gearGlow" cx="1" cy="1" r="1">
          <stop offset="0" stop-color="#c9681a" stop-opacity="0.75"/>
          <stop offset="1" stop-color="#f28a23" stop-opacity="0"/>
        </radialGradient>
      </defs>
      <path d="M31,31 H465 V66 C380,80 300,140 220,200 C150,250 80,270 31,276 Z" fill="var(--orange)"/>
      <path d="M31,286 C80,280 150,260 220,210 C300,150 380,90 465,76" fill="none" stroke="var(--stripe)" stroke-width="9"/>
      <path d="M31,514 C100,500 170,440 240,400 C320,350 400,310 465,300 V813 H31 Z" fill="var(--orange)"/>
      <path d="M31,504 C100,490 170,430 240,390 C320,340 400,300 465,290" fill="none" stroke="var(--stripe)" stroke-width="9"/>
      <g stroke="var(--ink)" stroke-width="3">
        <line x1="54" y1="132" x2="266" y2="132"/>
        <line x1="54" y1="147" x2="238" y2="147"/>
        <line x1="54" y1="162" x2="214" y2="162"/>
        <line x1="54" y1="177" x2="186" y2="177"/>
        <line x1="54" y1="192" x2="162" y2="192"/>
        <line x1="54" y1="207" x2="138" y2="207"/>
        <line x1="54" y1="222" x2="110" y2="222"/>
        <line x1="54" y1="237" x2="86" y2="237"/>
        <line x1="414" y1="334" x2="446" y2="334"/>
        <line x1="386" y1="349" x2="446" y2="349"/>
        <line x1="362" y1="364" x2="446" y2="364"/>
        <line x1="338" y1="379" x2="446" y2="379"/>
        <line x1="312" y1="394" x2="446" y2="394"/>
        <line x1="286" y1="409" x2="446" y2="409"/>
        <line x1="260" y1="424" x2="446" y2="424"/>
        <line x1="234" y1="439" x2="446" y2="439"/>
      </g>
      <g stroke="var(--ink)" stroke-width="2.5" fill="none" stroke-dasharray="7 5">
        <path d="M378,624 H262 Q254,624 254,632 V680"/>
      </g>
      <circle cx="378" cy="624" r="6" fill="var(--ink)"/>
      <path d="M246,680 H262 V686 H246 Z" fill="var(--ink)"/>
      <rect x="330" y="566" width="135" height="247" fill="url(#gearGlow)" role="img" aria-label="Cluster of bicycle gears and cogs decoration"/>
    </svg>
    <div class="wordmark">TWINE CIDER CO.</div>
    <div class="script script--hard">hard</div>
    <div class="script script--variety">apple cider</div>
    <div class="style-name">DRY</div>
    <div class="abv">
      <svg width="16" height="32" viewBox="0 0 16 32" aria-hidden="true">
        <rect x="5" y="1" width="6" height="22" rx="3" fill="var(--ink)"/>
        <circle cx="8" cy="25" r="6" fill="var(--ink)"/>
      </svg>
      <span>7% alc./vol.</span>
    </div>
  </section>

  <section class="label label--back">
    <svg class="label__art" viewBox="0 0 496 834" aria-hidden="true">
      <defs>
        <linearGradient id="gearFade" x1="0" y1="0" x2="1" y2="1">
          <stop offset="0" stop-color="#c8ab7c" stop-opacity="0.15"/>
          <stop offset="0.6" stop-color="#c8ab7c" stop-opacity="0.45"/>
          <stop offset="1" stop-color="#c8ab7c" stop-opacity="0.1"/>
        </linearGradient>
      </defs>
      <path d="M31,302 C100,300 170,340 240,390 C320,450 400,500 466,514 V813 H31 Z" fill="var(--orange)"/>
      <path d="M31,292 C100,290 170,330 240,380 C320,440 400,490 466,504" fill="none" stroke="var(--stripe)" stroke-width="9"/>
      <path d="M85,290 C150,280 220,300 280,340 C330,370 380,410 420,430 L420,470 C370,450 320,420 270,385 C210,345 150,315 85,300 Z" fill="url(#gearFade)" role="img" aria-label="Faint row of gears following the curve"/>
    </svg>
    <div class="wordmark">TWINE CIDER CO.</div>
    <p class="warning">
      GOVERNMENT WARNING:<br>
      (1) ACCORDING TO THE SURGEON GENERAL, WOMEN SHOULD<br>
      NOT DRINK ALCOHOLIC BEVERAGES DURING PREGNANCY<br>
      BECAUSE OF THE RISK OF BIRTH DEFECTS.<br>
      (2)CONSUMPTION OF ALCOHOLIC BEVERAGES IMPAIRS YOUR<br>
      ABILITY TO DRIVE A CAR OR OPERATE MACHINERY, AND MAY<br>
      CAUSE HEALTH PROBLEMS.
    </p>
    <p class="back-note back-note--sulfites">CONTAINS SULFITES</p>
    <p class="back-note back-note--bottler">VINTED + BOTTLED BY TWINE CIDER HALVERTON, CA</p>
  </section>

</main>
</body>
</html>
```